Lanterns Over the Silent Harbor

This book cover must convey the fact that the scientific evidence is clear that the afterlife is a reality. Attached are two ideas, but they're not working for me as they are. It could be that I'm not a graphic artist and can't get the composition correct. If there is a view of the afterlife, it must be realistic. The afterlife is just like this life. We can't use the family photo. I don't have permission.

```html
<!DOCTYPE html>
<html lang="en">
<head>
<meta charset="UTF-8">
<title>Lanterns Over the Silent Harbor — Book Cover</title>
<link rel="stylesheet" href="https://fonts.googleapis.com/css2?family=Cinzel:wght@400;500&family=Marcellus&display=swap">
<style>
  :root {
    --page-bg: #ececee;
    --cover-blue-deep: #1d4a86;
    --cover-blue: #2c64a6;
    --cover-blue-light: #6f9bd0;
    --cover-mist: #e4edf7;
    --glow-core: #fff6ea;
    --glow-peach: #f6c9a6;
    --glow-rose: #e79a86;
    --glow-violet: #9d8fc4;
    --title-white: #ffffff;
    --title-gold: #f0c98a;
    --author-ink: #1b2436;
  }

  * { margin: 0; padding: 0; box-sizing: border-box; }

  html, body {
    width: 1200px;
    height: 1200px;
    overflow: hidden;
    background: var(--page-bg);
  }

  .canvas {
    position: relative;
    width: 1200px;
    height: 1200px;
    display: flex;
    align-items: center;
    justify-content: center;
  }

  .book-cover {
    position: relative;
    width: 756px;
    height: 1100px;
    overflow: hidden;
    background: linear-gradient(180deg,
      var(--cover-blue-deep) 0%,
      var(--cover-blue) 40%,
      var(--cover-blue-light) 75%,
      var(--cover-mist) 100%);
  }

  .cover-art {
    position: absolute;
    left: 0;
    top: 340px;
    width: 756px;
    height: 760px;
    background:
      radial-gradient(circle at 50% 50%,
        var(--glow-core) 0%,
        var(--glow-peach) 18%,
        var(--glow-rose) 30%,
        var(--glow-violet) 42%,
        rgba(111,155,208,0.55) 56%,
        rgba(44,100,166,0) 72%),
      linear-gradient(180deg, rgba(255,255,255,0) 60%, var(--cover-mist) 100%);
  }

  .cover-title {
    position: absolute;
    top: 80px;
    left: 0;
    width: 100%;
    text-align: center;
    font-family: "Cinzel", "Times New Roman", serif;
    color: var(--title-white);
    line-height: 1;
  }

  .title-main {
    display: block;
    font-size: 104px;
    font-weight: 400;
    letter-spacing: 2px;
    text-shadow: 0 2px 6px rgba(10,30,70,0.35);
  }

  .title-middle {
    display: block;
    margin-top: 34px;
    font-size: 46px;
    font-weight: 400;
    letter-spacing: 2px;
    color: var(--title-gold);
  }

  .title-end {
    display: block;
    margin-top: 30px;
    font-size: 104px;
    font-weight: 400;
    letter-spacing: 3px;
    text-shadow: 0 2px 6px rgba(10,30,70,0.35);
  }

  .cover-author {
    position: absolute;
    bottom: 44px;
    left: 0;
    width: 100%;
    text-align: center;
    font-family: "Marcellus", "Times New Roman", serif;
    font-size: 38px;
    letter-spacing: 0.5px;
    color: var(--author-ink);
  }
</style>
</head>
<body>
  <main class="canvas">
    <section class="book-cover">
      <div class="cover-art" role="img" aria-label="Radiant tunnel of light with a smiling family and their puppy at its glowing centre"></div>

      <h1 class="cover-title">
        <span class="title-main">LANTERNS</span>
        <span class="title-middle">OVER THE SILENT</span>
        <span class="title-end">HARBOR</span>
      </h1>

      <p class="cover-author">R. Calvin Harlow, PhD</p>
    </section>
  </main>
</body>
</html>
```